Bright Meadow Counseling Business Card design with a visually interesting use of Space

I need business cards that are luxurious and give a peaceful, calm vibe. I also had some letterhead designed, and i like the look of it also, it's attached with the logo design for reference/ ideas but feel free to be creative.

Target Market(s)

High end luxurious client who needs counseling

Industry/Entity Type

Marriage and Family Therapy

Contact Information for Business Card

Mira Kowalczyk MS LMFT/ or Toby Hallett address 4150 Larkin Suite 600

Font styles to use
Sans Serif

Colors
0054AA
0677BA
7BADD7
CADEEF
E8F1F8
0094D4
00A9DD
6FCCEA
C7EBF8
E9F6FB
A7469A
B969AE
D3A5CF
EDDBEB
F8F0F9
6B429C
8869AF
B7A5CE
E3DAEB
F3F0F8

Requirements
Must have
• Logo and color scheme but be simple modern and luxurious
Nice to have
• I'd like to incorporate some elelmets from the logo and letterhead into a simple modern card

```html
<!DOCTYPE html>
<html lang="en">
<head>
<meta charset="utf-8">
<title>Bright Meadow Counseling – Business Card</title>
<link rel="stylesheet" href="https://fonts.googleapis.com/css2?family=Josefin+Sans:wght@300&family=Lexend:wght@300&display=swap">
<style>
  :root {
    --stage: #141414;
    --card-purple: #9b49ad;
    --gold: #d9a92a;
    --gold-deep: #b8861c;
    --card-white: #ffffff;
    --mist-blue: #e4eff8;
    --mist-teal: #e9f6fb;
    --mist-pink: #f3e6f1;
    --accent-violet: #8869af;
  }
  * { margin: 0; padding: 0; box-sizing: border-box; }
  html, body { width: 1200px; height: 800px; overflow: hidden; }
  body {
    background: var(--stage);
    position: relative;
    font-family: "Lexend", sans-serif;
  }
  .card {
    position: absolute;
    top: 245px;
    width: 540px;
    height: 310px;
    border-radius: 22px;
    overflow: hidden;
  }

  /* Back of card: purple with gold emblem and contact details */
  .card-back {
    left: 40px;
    background: var(--card-purple);
    color: var(--gold);
  }
  .back-mark {
    position: absolute;
    top: 28px;
    right: 40px;
    display: flex;
    flex-direction: column;
    align-items: center;
    gap: 10px;
  }
  .emblem-circle {
    width: 150px;
    height: 150px;
    border-radius: 50%;
    background: var(--gold);
  }
  .mark-name {
    font-family: "Josefin Sans", sans-serif;
    font-weight: 300;
    font-size: 13px;
    letter-spacing: 1px;
    color: var(--gold);
  }
  .contact-block {
    position: absolute;
    left: 36px;
    bottom: 34px;
  }
  .holder-name {
    font-size: 24px;
    font-weight: 300;
    margin-bottom: 8px;
  }
  .holder-name .credentials {
    font-size: 14px;
    margin-left: 6px;
  }
  .contact-list { list-style: none; }
  .contact-list li {
    display: flex;
    align-items: center;
    gap: 8px;
    font-size: 12px;
    font-weight: 300;
    line-height: 19px;
  }
  .contact-list svg { width: 10px; height: 10px; fill: var(--gold); flex: none; }

  /* Front of card: white with wordmark */
  .card-front {
    left: 620px;
    background: var(--card-white);
  }
  .front-wash {
    position: absolute;
    inset: 0;
    background: linear-gradient(160deg, var(--card-white) 30%, var(--mist-teal) 55%, var(--mist-blue) 75%, var(--mist-pink) 100%);
  }
  .front-dot {
    position: absolute;
    top: 40px;
    right: 70px;
    width: 64px;
    height: 64px;
    border-radius: 50%;
    background: var(--accent-violet);
  }
  .wordmark {
    position: absolute;
    left: 0;
    right: 0;
    top: 150px;
    text-align: center;
    font-family: "Josefin Sans", sans-serif;
    font-weight: 300;
    color: var(--gold-deep);
    font-size: 40px;
    letter-spacing: 1px;
  }
</style>
</head>
<body>
  <section class="card card-back">
    <div class="back-mark">
      <span class="emblem-circle"></span>
      <span class="mark-name">Bright Meadow Counseling</span>
    </div>
    <div class="contact-block">
      <p class="holder-name">Mira Kowalczyk<span class="credentials">MS LMFT</span></p>
      <ul class="contact-list">
        <li><svg viewBox="0 0 10 10"><path d="M2 0.5l2 2-1 1.2c.6 1.3 1.6 2.3 2.9 2.9L7 5.6l2 2-1.3 1.6C4.3 9 1 5.7.7 2.1z"/></svg>555.204.7318</li>
        <li><svg viewBox="0 0 10 10"><path d="M0 2h10v6H0z"/></svg>mira@BrightMeadowCounseling.com</li>
        <li><svg viewBox="0 0 10 10"><circle cx="5" cy="5" r="4.5"/></svg>BrightMeadowCounseling.com</li>
        <li><svg viewBox="0 0 10 10"><path d="M5 0a3.5 3.5 0 0 1 3.5 3.5C8.5 6 5 10 5 10S1.5 6 1.5 3.5A3.5 3.5 0 0 1 5 0z"/></svg>4150 Larkin Ave</li>
      </ul>
    </div>
  </section>

  <section class="card card-front">
    <div class="front-wash" role="img" aria-label="Soft pastel backdrop in pale blue, teal and pink tones"></div>
    <span class="front-dot"></span>
    <p class="wordmark">Bright Meadow Counseling</p>
  </section>
</body>
</html>
```